Wine Label Design for the red wine named “Amber Moth Ridge” or “A/M”

Create an elegant yet simple (less is more) label for a red, full-bodied wine from a family-owned Herzegovinian vineyard by the river with 9 names. You can use elements such as the Calopteryx virgo, possibly the river shape, and ensure a coherent storytelling of the unique vineyard’s locality and meticulous, hand-picked grape cultivation.
Let’s craft a label that is not just seen, but is experienced and remembered.

Target Market(s)

Wine lovers that appreciate high quality wines

Industry/Entity Type

Wine, Family owned small producer

Requirements
Must have
• Name A/M, front and back label. Premium feel, uniqueness. Simple but interesting.
Nice to have
• Please see the images below as an idea of various directions. I am also leaning to embossed image on the label
Should not have
• Should not be overcrowded with text, too many images and objects

```html
<!DOCTYPE html>
<html lang="en">
<head>
<meta charset="utf-8">
<title>Amber Moth Ridge – Red Wine Label Range</title>
<link rel="stylesheet" href="https://fonts.googleapis.com/css2?family=Bodoni+Moda:wght@400;700&family=Montserrat:wght@300;400&display=swap">
<style>
  :root {
    --page: #ffffff;
    --brand-blue: #2f9be0;
    --brand-blue-light: #5db7ee;
    --capsule-paper: #eeeeee;
    --capsule-night: #111111;
    --label-paper: #ececec;
    --label-night: #2a2a2a;
    --label-sky: #4aaee9;
    --ink-white: #ffffff;
  }
  * { margin: 0; padding: 0; box-sizing: border-box; }
  html, body {
    width: 1200px; height: 1200px; overflow: hidden;
    background: var(--page);
  }
  .range {
    width: 1200px; height: 1200px;
    display: flex; justify-content: center; align-items: center;
    gap: 45px;
  }
  .variant {
    width: 330px;
    display: flex; flex-direction: column; align-items: center; gap: 50px;
  }
  .neck-band {
    width: 140px; height: 120px;
    display: flex; align-items: center; justify-content: center;
    font-family: "Bodoni Moda", serif; font-weight: 400;
    font-size: 40px; letter-spacing: 2px;
  }
  .label {
    width: 330px; height: 440px;
    padding: 70px 22px 24px;
    display: flex; flex-direction: column;
  }
  .wordmark {
    font-family: "Bodoni Moda", serif; font-weight: 400;
    font-size: 62px; line-height: 1.05; letter-spacing: 1px;
    text-transform: uppercase; text-align: center;
  }
  .wordmark span { display: block; }
  .facts {
    margin-top: auto;
    display: grid; grid-template-columns: 1fr auto 1fr; align-items: end;
    font-family: "Montserrat", sans-serif; font-weight: 300;
  }
  .facts .volume, .facts .abv { font-size: 11px; padding-bottom: 4px; }
  .facts .abv { text-align: right; }
  .wine-type { text-align: center; }
  .wine-type .style {
    display: block;
    font-family: "Bodoni Moda", serif; font-weight: 700;
    font-size: 20px; letter-spacing: 1px;
  }
  .wine-type .region { display: block; font-size: 12px; letter-spacing: 1px; }

  .variant--paper .neck-band { background: var(--capsule-paper); color: var(--brand-blue); }
  .variant--paper .label { background: var(--label-paper); color: var(--brand-blue); }

  .variant--night .neck-band { background: var(--capsule-night); color: var(--brand-blue); }
  .variant--night .label { background: var(--label-night); color: var(--brand-blue-light); }

  .variant--sky .neck-band { background: var(--brand-blue); color: var(--ink-white); }
  .variant--sky .label { background: var(--label-sky); color: var(--ink-white); }
</style>
</head>
<body>
<main class="range">
  <section class="variant variant--paper">
    <div class="neck-band">A/M</div>
    <div class="label">
      <h1 class="wordmark"><span>Amber</span><span>Moth</span><span>Ridge</span></h1>
      <div class="facts">
        <span class="volume">750 ml</span>
        <p class="wine-type"><span class="style">RED WINE</span><span class="region">HERZEGOVINA</span></p>
        <span class="abv">13% vol</span>
      </div>
    </div>
  </section>

  <section class="variant variant--night">
    <div class="neck-band">A/M</div>
    <div class="label">
      <h1 class="wordmark"><span>Amber</span><span>Moth</span><span>Ridge</span></h1>
      <div class="facts">
        <span class="volume">750 ml</span>
        <p class="wine-type"><span class="style">RED WINE</span><span class="region">HERZEGOVINA</span></p>
        <span class="abv">13% vol</span>
      </div>
    </div>
  </section>

  <section class="variant variant--sky">
    <div class="neck-band">A/M</div>
    <div class="label">
      <h1 class="wordmark"><span>Amber</span><span>Moth</span><span>Ridge</span></h1>
      <div class="facts">
        <span class="volume">750 ml</span>
        <p class="wine-type"><span class="style">RED WINE</span><span class="region">HERZEGOVINA</span></p>
        <span class="abv">13% vol</span>
      </div>
    </div>
  </section>
</main>
</body>
</html>
```